Simple graphic for a book or slide presentation

We are looking for a style that suits the style of our book. It's title is Venture. Thriving boldly on uncertain ground. There will be more line drawing/graphics in the book but how you design this image will create the style for all the other simple graphics in the book (once we decide what they are). So this one design will lead to a few more to match the style of this one. We'd like the shape of the overall graphic (i.e the arrows and words/bubbles) to be circular (not a rounded square as appears in the sample attached). Perhaps the words don't need to be in ovals or bound by anything at all; perhaps they do - let's see what you see. We'd like you to choose a font or offer many different fonts you think will capture the practical yet unconventional tone of the book. The book is teaching that managing risks in life is a life-skill that can be learned. The section of the book where this graphic will be placed is called "the power of language" - basically we are saying that thoughts, words and actions create our culture and our destiny. This insight comes from Pranav Kelkari's famous quote:
Carefully watch your thoughts, for they become your words.
Manage and watch your words, for they will become your actions.
Consider and judge your actions, for they have become your habits.
Acknowledge and watch your habits, for they shall become your values.
Understand and embrace your values, for they become your destiny.

Please change the text in the middle of the graphic to say: The Human Culture Cycle

```html
<!DOCTYPE html>
<html lang="en">
<head>
<meta charset="utf-8">
<title>The Human Culture Cycle</title>
<link rel="stylesheet" href="https://fonts.googleapis.com/css2?family=Arimo:wght@400;700&family=Roboto+Condensed:wght@400&display=swap">
<style>
  :root {
    --yellow: #fecb0a;
    --orange: #fbad1a;
    --navy: #1e5f8f;
    --sky: #27b1e5;
    --lime: #83c341;
    --green: #2fb24b;
    --title-blue: #2e6f98;
    --grey-1: #a7a8ab;
    --grey-2: #96979b;
    --grey-3: #85868a;
    --grey-4: #6e6f73;
    --grey-5: #58585a;
    --grey-6: #39393b;
    --label: #f4f4f4;
    --ink: #333335;
    --caption: #4a4a4a;
    --paper: #ffffff;
  }
  html, body {
    margin: 0;
    padding: 0;
    width: 1200px;
    height: 1200px;
    overflow: hidden;
    background: var(--paper);
  }
  .canvas { display: block; width: 1200px; height: 1200px; }
  .node-label {
    font-family: "Arimo", Arial, sans-serif;
    font-weight: 700;
    font-size: 54px;
    fill: var(--label);
    text-anchor: middle;
    dominant-baseline: central;
  }
  .cycle-title {
    font-family: "Arimo", Arial, sans-serif;
    font-size: 58px;
    text-anchor: middle;
  }
  .cycle-title--colour { font-weight: 700; fill: var(--title-blue); }
  .cycle-title--mono { font-weight: 400; fill: var(--ink); }
  .shaft { fill: none; stroke-width: 15; }
  .swatch-code, .swatch-caption {
    font-family: "Roboto Condensed", "Arial Narrow", sans-serif;
    fill: var(--caption);
  }
  .swatch-code { font-size: 15px; text-anchor: middle; }
  .swatch-caption { font-size: 16px; }
</style>
</head>
<body>
<svg class="canvas" viewBox="0 0 1920 1920" xmlns="http://www.w3.org/2000/svg" role="img" aria-label="The Human Culture Cycle: thoughts, words, actions, habits, values, culture">

  <!-- Colour cycle -->
  <g class="cycle cycle--colour">
    <g class="arrows">
      <path class="shaft" style="stroke:var(--green)" d="M345,296 Q370,276 400,258"/>
      <path style="fill:var(--green)" d="M445,237 Q405,250 362,232 L396,262 L400,305 Q415,265 445,237 Z"/>
      <path class="shaft" style="stroke:var(--yellow)" d="M712,232 Q745,244 770,262"/>
      <path style="fill:var(--yellow)" d="M820,288 Q800,265 785,215 L770,264 L738,284 Q780,275 820,288 Z"/>
      <path class="shaft" style="stroke:var(--orange)" d="M955,530 Q962,560 960,590"/>
      <path style="fill:var(--orange)" d="M953,648 Q940,610 918,573 L958,592 L1000,580 Q970,605 953,648 Z"/>
      <path class="shaft" style="stroke:var(--navy)" d="M808,877 Q785,893 758,906"/>
      <path style="fill:var(--navy)" d="M707,929 Q740,905 755,863 L757,907 L788,940 Q750,922 707,929 Z"/>
      <path class="shaft" style="stroke:var(--sky)" d="M443,920 Q415,907 392,893"/>
      <path style="fill:var(--sky)" d="M347,857 Q390,873 428,868 L395,885 L378,933 Q370,890 347,857 Z"/>
      <path class="shaft" style="stroke:var(--lime)" d="M220,630 Q215,600 216,585"/>
      <path style="fill:var(--lime)" d="M220,525 Q235,570 257,599 L218,585 L175,593 Q205,560 220,525 Z"/>
    </g>
    <g class="nodes">
      <circle cx="571" cy="230" r="117" style="fill:var(--yellow)"/>
      <text class="node-label" x="571" y="230" textLength="202" lengthAdjust="spacingAndGlyphs">Thoughts</text>
      <circle cx="875" cy="408" r="117" style="fill:var(--orange)"/>
      <text class="node-label" x="876" y="408" textLength="162" lengthAdjust="spacingAndGlyphs">Words</text>
      <circle cx="878" cy="755" r="117" style="fill:var(--navy)"/>
      <text class="node-label" x="878" y="755" textLength="190" lengthAdjust="spacingAndGlyphs">Actions</text>
      <circle cx="573" cy="934" r="117" style="fill:var(--sky)"/>
      <text class="node-label" x="577" y="942" textLength="159" lengthAdjust="spacingAndGlyphs">Habits</text>
      <circle cx="263" cy="751" r="117" style="fill:var(--lime)"/>
      <text class="node-label" x="267" y="749" textLength="165" lengthAdjust="spacingAndGlyphs">Values</text>
      <circle cx="263" cy="408" r="117" style="fill:var(--green)"/>
      <text class="node-label" x="264" y="405" textLength="182" lengthAdjust="spacingAndGlyphs">Culture</text>
    </g>
    <text class="cycle-title cycle-title--colour"><tspan x="572" y="496">The</tspan><tspan x="572" y="554">Human</tspan><tspan x="572" y="612">Culture</tspan><tspan x="572" y="670">Cycle</tspan></text>
  </g>

  <!-- Greyscale cycle -->
  <g class="cycle cycle--mono" transform="translate(774,788)">
    <g class="arrows">
      <path class="shaft" style="stroke:var(--grey-6)" d="M345,296 Q370,276 400,258"/>
      <path style="fill:var(--grey-6)" d="M445,237 Q405,250 362,232 L396,262 L400,305 Q415,265 445,237 Z"/>
      <path class="shaft" style="stroke:var(--grey-1)" d="M712,232 Q745,244 770,262"/>
      <path style="fill:var(--grey-1)" d="M820,288 Q800,265 785,215 L770,264 L738,284 Q780,275 820,288 Z"/>
      <path class="shaft" style="stroke:var(--grey-2)" d="M955,530 Q962,560 960,590"/>
      <path style="fill:var(--grey-2)" d="M953,648 Q940,610 918,573 L958,592 L1000,580 Q970,605 953,648 Z"/>
      <path class="shaft" style="stroke:var(--grey-3)" d="M808,877 Q785,893 758,906"/>
      <path style="fill:var(--grey-3)" d="M707,929 Q740,905 755,863 L757,907 L788,940 Q750,922 707,929 Z"/>
      <path class="shaft" style="stroke:var(--grey-4)" d="M443,920 Q415,907 392,893"/>
      <path style="fill:var(--grey-4)" d="M347,857 Q390,873 428,868 L395,885 L378,933 Q370,890 347,857 Z"/>
      <path class="shaft" style="stroke:var(--grey-5)" d="M220,630 Q215,600 216,585"/>
      <path style="fill:var(--grey-5)" d="M220,525 Q235,570 257,599 L218,585 L175,593 Q205,560 220,525 Z"/>
    </g>
    <g class="nodes">
      <circle cx="571" cy="230" r="117" style="fill:var(--grey-1)"/>
      <text class="node-label" x="571" y="230" textLength="202" lengthAdjust="spacingAndGlyphs">Thoughts</text>
      <circle cx="875" cy="408" r="117" style="fill:var(--grey-2)"/>
      <text class="node-label" x="876" y="408" textLength="162" lengthAdjust="spacingAndGlyphs">Words</text>
      <circle cx="878" cy="755" r="117" style="fill:var(--grey-3)"/>
      <text class="node-label" x="878" y="755" textLength="190" lengthAdjust="spacingAndGlyphs">Actions</text>
      <circle cx="573" cy="934" r="117" style="fill:var(--grey-4)"/>
      <text class="node-label" x="577" y="942" textLength="159" lengthAdjust="spacingAndGlyphs">Habits</text>
      <circle cx="263" cy="751" r="117" style="fill:var(--grey-5)"/>
      <text class="node-label" x="267" y="749" textLength="165" lengthAdjust="spacingAndGlyphs">Values</text>
      <circle cx="263" cy="408" r="117" style="fill:var(--grey-6)"/>
      <text class="node-label" x="264" y="405" textLength="182" lengthAdjust="spacingAndGlyphs">Culture</text>
    </g>
    <text class="cycle-title cycle-title--mono"><tspan x="572" y="496">The</tspan><tspan x="572" y="554">Human</tspan><tspan x="572" y="612">Culture</tspan><tspan x="572" y="670">Cycle</tspan></text>
  </g>

  <!-- Palette key -->
  <g class="palette-key">
    <rect x="1263" y="62" width="89" height="239" style="fill:var(--yellow)"/>
    <rect x="1362" y="62" width="89" height="239" style="fill:var(--orange)"/>
    <rect x="1461" y="62" width="89" height="239" style="fill:var(--navy)"/>
    <rect x="1559" y="62" width="89" height="239" style="fill:var(--sky)"/>
    <rect x="1658" y="62" width="89" height="239" style="fill:var(--lime)"/>
    <rect x="1757" y="62" width="89" height="239" style="fill:var(--green)"/>
    <text class="swatch-code" x="1307" y="318">#FFC200</text>
    <text class="swatch-code" x="1406" y="318">#FEA002</text>
    <text class="swatch-code" x="1505" y="318">#174B7D</text>
    <text class="swatch-code" x="1604" y="318">#19A3EB</text>
    <text class="swatch-code" x="1703" y="318">#67DD0B</text>
    <text class="swatch-code" x="1797" y="318">#25A800</text>
    <text class="swatch-caption" x="1263" y="348">Happy 15 August Color Scheme</text>
  </g>
</svg>
</body>
</html>
```